Bellmoor Commercial Finance Information Brochure

This brochure will be sent out to clients via A4 PDF on an email to showcase what our company has to offer. We are a commercial finance brokerage, that specialises in property finance. We would like to see designs following our colour scheme. The final design should demonstrate our professionalism and reliability.
I have attached our logo and also a few bullet points on our information and what we can offer. These can be slightly reworded for conciseness. Or leave the text sections as filler and I can fill these in.
I have also attached an overview of our colour scheme and design styling for your consideration.
Target Market(s)
Property Developers
Industry/Entity Type
Financial Services

```html
<!DOCTYPE html>
<html lang="en">
<head>
<meta charset="utf-8">
<title>Bellmoor Commercial Finance – Information Brochure</title>
<link href="https://fonts.googleapis.com/css2?family=Roboto+Condensed:wght@400;700&display=swap" rel="stylesheet">
<style>
  :root{
    --backdrop:#6175a9;
    --paper:#f9f9fb;
    --navy:#1f3f9c;
    --green:#1f8a3c;
    --sky:#2a73c1;
    --ink:#1b1b1f;
    --tile:#e2e2ef;
  }
  *{margin:0;padding:0;box-sizing:border-box}
  html,body{width:1200px;height:898px;overflow:hidden}
  body{background:var(--backdrop);font-family:"Roboto Condensed",Arial,sans-serif;color:var(--ink)}
  .page{position:absolute;left:296px;top:18px;width:608px;height:862px;background:var(--paper);overflow:hidden}

  .brand{position:absolute;top:28px;left:0;width:100%;text-align:center;color:var(--navy);font-weight:700;font-size:27px;line-height:1;letter-spacing:.5px}
  .brand small{display:block;font-size:12px;letter-spacing:5px;margin-top:6px}

  .hero{position:absolute;left:0;top:93px;width:608px;height:266px;
    background:linear-gradient(100deg,#2f3d66 0%,#8c95b4 22%,#c9ccd6 45%,#d9dadd 65%,#a7a9ad 82%,#e0512a 90%,#3a3838 100%)}

  .banner{position:absolute;left:27px;color:#fff;font-weight:700;text-transform:uppercase;display:flex;align-items:center;padding-left:23px;font-size:23px}
  .banner--question{top:313px;width:284px;height:40px;background:var(--navy)}
  .banner--answer{top:353px;width:413px;height:47px;background:var(--green)}

  .intro{position:absolute;left:23px;top:416px;width:565px;font-size:11px;line-height:14.4px;text-align:justify}
  .intro p+p{margin-top:9px}
  .intro strong{font-weight:700}

  .why-title{position:absolute;top:580px;left:0;width:100%;text-align:center;color:var(--green);font-weight:700;font-size:17.5px}

  .tile{position:absolute;top:608px;height:114px;background:var(--tile);text-align:center;color:var(--navy);padding-top:8px}
  .tile h3{font-size:17.5px;font-weight:700;display:flex;justify-content:center;align-items:center;gap:4px;margin-bottom:4px}
  .tile p{font-size:11px;line-height:14.3px;padding:0 8px}
  .tile--efficiency{left:10px;width:190px}
  .tile--experience{left:206px;width:192px}
  .tile--reliability{left:405px;width:192px}

  .services{position:absolute;left:19px;top:746px;width:569px;height:57px;border:1px solid var(--navy);border-bottom:none}
  .services-label{position:absolute;top:-9px;left:50%;transform:translateX(-50%);background:var(--paper);padding:0 12px;color:var(--navy);font-weight:700;font-size:12px;white-space:nowrap}
  .service{position:absolute;top:14px;width:149px;height:25px;border-radius:3px;color:#fff;font-weight:700;font-size:11.5px;display:flex;align-items:center;justify-content:center}
  .service--bridge{left:48px;background:var(--navy)}
  .service--development{left:207px;background:var(--green)}
  .service--btl{left:362px;background:var(--sky)}

  .contact{position:absolute;left:16px;color:var(--navy);font-weight:700;font-size:11px;display:flex;align-items:center;gap:4px}
  .contact--address{top:812px}
  .contact--lines{top:830px;gap:4px}
  .contact svg{flex:none}

  .hotline{position:absolute;right:17px;top:810px;display:flex;align-items:center;gap:8px}
  .hotline-text{line-height:1}
  .hotline-text span{display:block;color:var(--green);font-weight:700;font-size:11px;margin-bottom:2px}
  .hotline-text strong{color:var(--navy);font-size:20px;font-weight:700}
</style>
</head>
<body>
<main class="page">
  <div class="brand">BELLMOOR<small>FINANCE</small></div>

  <div class="hero" role="img" aria-label="Photo of a business handshake blended with a construction worker in a hi-vis vest inside a rail tunnel"></div>

  <div class="banner banner--question">What sets us apart?</div>
  <div class="banner banner--answer">Well, we've walked in your shoes.</div>

  <section class="intro">
    <p>As former lenders and developers ourselves, we intimately understand the inefficiencies that plague many brokers in the market today. We’ve experienced the frustration of tight time limits on deals and the exasperating feeling of brokers wasting precious time collecting information. <strong>It’s enough to drive developers and lenders insane!</strong></p>
    <p><strong>That’s why we founded Bellmoor Finance - to be the efficient and reliable link that connects developers and lenders.</strong> We’ve streamlined our processes to eliminate unnecessary hurdles, enabling clear and swift communication between all parties involved. <strong>No more wasted time. No more unnecessary stress.</strong></p>
    <p>With our expertise and industry insights, we’ve developed a unique approach that simplifies the financing journey. <strong>From the initial consultation to the final funding, we’re here to guide you every step of the way. Our goal? To make commercial financing a smooth and enjoyable experience for you.</strong></p>
  </section>

  <h2 class="why-title">Why choose Bellmoor Commercial Finance?</h2>

  <article class="tile tile--efficiency">
    <h3><svg width="15" height="15" viewBox="0 0 16 16"><circle cx="8" cy="8" r="7" fill="none" stroke="var(--green)" stroke-width="1.3"/><path d="M4.8 8.2l2.2 2.1 4.2-4.4" fill="none" stroke="var(--green)" stroke-width="1.3"/></svg>Efficiency</h3>
    <p>Our main business strategy is to reduce the amount of man-hours spent organising deals for lender and developers. Bellmoor Commercial Finance do all the hard work for you.</p>
  </article>
  <article class="tile tile--experience">
    <h3><svg width="15" height="15" viewBox="0 0 16 16"><circle cx="8" cy="8" r="7" fill="none" stroke="var(--green)" stroke-width="1.3"/><path d="M4.8 8.2l2.2 2.1 4.2-4.4" fill="none" stroke="var(--green)" stroke-width="1.3"/></svg>Experience</h3>
    <p>Having been on both side of the financing world, our experience in the structuring of various deals allows us to provide our clients with options no other broker can provide.</p>
  </article>
  <article class="tile tile--reliability">
    <h3><svg width="15" height="15" viewBox="0 0 16 16"><circle cx="8" cy="8" r="7" fill="none" stroke="var(--green)" stroke-width="1.3"/><path d="M4.8 8.2l2.2 2.1 4.2-4.4" fill="none" stroke="var(--green)" stroke-width="1.3"/></svg>Reliability</h3>
    <p>Having established relationships with lenders and developers alike, through our dealings in both sectors, we pride our self on being able to deliver as promised.</p>
  </article>

  <section class="services">
    <div class="services-label">Please contact us for any questions related to:</div>
    <div class="service service--bridge">BRIDGE LOANS</div>
    <div class="service service--development">DEVELOPMENT FINANCE</div>
    <div class="service service--btl">BUY-TO-LET MORTGAGES</div>
  </section>

  <div class="contact contact--address">
    <svg width="8" height="11" viewBox="0 0 8 11"><path d="M4 0a4 4 0 0 0-4 4c0 3 4 7 4 7s4-4 4-7a4 4 0 0 0-4-4z" fill="var(--green)"/><circle cx="4" cy="4" r="1.4" fill="#fff"/></svg>
    2140 Larchfield Road Juneau, Alaska 99801
  </div>
  <div class="contact contact--lines">
    <svg width="7" height="11" viewBox="0 0 7 11"><rect x=".6" y=".6" width="5.8" height="9.8" rx="1" fill="none" stroke="var(--green)" stroke-width="1.2"/></svg>
    <span>555-201-4830</span>
    <svg width="10" height="7" viewBox="0 0 10 7" style="margin-left:4px"><rect width="10" height="7" fill="var(--green)"/><path d="M0 0l5 4 5-4" fill="none" stroke="#fff" stroke-width="1"/></svg>
    <span>info@bellmoorfinance.com</span>
    <svg width="9" height="9" viewBox="0 0 10 10" style="margin-left:3px"><circle cx="5" cy="5" r="4.4" fill="none" stroke="var(--green)" stroke-width="1.1"/><path d="M.6 5h8.8M5 .6c-2.4 2.4-2.4 6.4 0 8.8M5 .6c2.4 2.4 2.4 6.4 0 8.8" fill="none" stroke="var(--green)" stroke-width=".9"/></svg>
    <span>www.bellmoorfinance.com</span>
  </div>

  <div class="hotline">
    <svg width="28" height="28" viewBox="0 0 28 28"><circle cx="14" cy="14" r="14" fill="var(--green)"/><path d="M9 8.5c.8-.8 1.6-.6 2 0l1.3 2c.4.6.2 1.2-.3 1.6l-.8.6c.7 1.6 2 2.9 3.6 3.6l.6-.8c.4-.5 1-.7 1.6-.3l2 1.3c.6.4.8 1.2 0 2-1.4 1.4-3.4 1.2-6-.8s-4.6-4.6-4.8-6.4c-.1-1.2.2-2.1.8-2.8z" fill="#fff"/></svg>
    <div class="hotline-text"><span>For mor info</span><strong>555-309-7716</strong></div>
  </div>
</main>
</body>
</html>
```